Sign Design

We already have a logo, but would like to design 2 x signs.
Sign 1:
Dimensions 1500mm wide x 2500m high.
Information to include on sign: - Clinic name and logo (attached)
- the word "DENTIST "
- Street number (which is 847)
Phone number (which is 6154 3970)

Sign 2:
Dimensions: 800mm wide x 600mm high

```html
<!DOCTYPE html>
<html lang="en">
<head>
<meta charset="utf-8">
<title>Wattlebrook Dental Care – Signage</title>
<link rel="stylesheet" href="https://fonts.googleapis.com/css2?family=Mulish:wght@400;600;700;800&display=swap">
<style>
  :root {
    --backdrop: #cccccc;
    --white: #ffffff;
    --green-dark: #177233;
    --green-bright: #12b01e;
    --green-mid: #9fdf4a;
    --green-pale: #dff5b0;
  }
  * { margin: 0; padding: 0; box-sizing: border-box; }
  html, body { width: 1200px; height: 900px; overflow: hidden; }
  body {
    background: var(--backdrop);
    font-family: "Mulish", sans-serif;
    color: var(--green-dark);
    position: relative;
  }

  /* Sign 1 – tall pylon sign */
  .sign-tall {
    position: absolute;
    left: 164px; top: 52px;
    width: 478px; height: 796px;
    background: var(--white);
  }
  .sign-tall .band-top,
  .sign-tall .band-bottom {
    position: absolute; left: 0; width: 100%; height: 27px;
    background: var(--green-pale);
  }
  .sign-tall .band-top { top: 0; }
  .sign-tall .band-bottom { bottom: 0; }
  .sign-tall .brand-mark {
    position: absolute; left: 89px; top: 88px;
    width: 300px; height: 300px; border-radius: 50%;
    background: var(--green-pale);
  }
  .sign-tall .brand-name {
    position: absolute; left: 0; top: 425px; width: 100%;
    text-align: center; font-weight: 400; color: var(--green-dark);
  }
  .sign-tall .brand-name .primary { display: block; font-size: 62px; line-height: 70px; letter-spacing: -1px; }
  .sign-tall .brand-name .secondary { display: block; font-size: 34px; line-height: 40px; }
  .sign-tall .service-band {
    position: absolute; left: 0; top: 556px; width: 100%; height: 75px;
    background: var(--green-pale);
    display: flex; align-items: center; justify-content: center;
  }
  .sign-tall .service {
    font-weight: 700; font-size: 58px; letter-spacing: 12px;
    margin-right: -12px; color: var(--green-dark);
  }
  .sign-tall .street {
    position: absolute; left: 0; top: 659px; width: 100%;
    text-align: center; font-weight: 600; font-size: 29px; letter-spacing: 1px;
  }
  .sign-tall .phone {
    position: absolute; left: 0; top: 700px; width: 100%;
    display: flex; align-items: center; justify-content: center; gap: 8px;
    font-weight: 700; font-size: 54px; line-height: 56px;
  }
  .sign-tall .phone svg { width: 34px; height: 44px; }

  /* Sign 2 – small wall sign */
  .sign-small {
    position: absolute;
    left: 780px; top: 354px;
    width: 256px; height: 192px;
    background: var(--white);
  }
  .sign-small .stripe { position: absolute; left: 0; width: 100%; }
  .stripe.dark { background: var(--green-bright); height: 14px; }
  .stripe.mid { background: var(--green-mid); height: 10px; }
  .stripe.pale { background: var(--green-pale); height: 10px; }
  .sign-small .brand-mark {
    position: absolute; left: 15px; top: 62px;
    width: 64px; height: 64px; border-radius: 50%;
    background: var(--green-pale);
  }
  .sign-small .brand-name {
    position: absolute; left: 88px; top: 66px;
    font-weight: 400; color: var(--green-dark); text-align: right;
  }
  .sign-small .brand-name .primary { display: block; font-size: 24px; line-height: 28px; letter-spacing: -0.5px; }
  .sign-small .brand-name .secondary { display: block; font-size: 14px; line-height: 16px; }
</style>
</head>
<body>

  <section class="sign-tall" aria-label="Pylon sign">
    <div class="band-top"></div>
    <div class="brand-mark"></div>
    <h1 class="brand-name">
      <span class="primary">Wattlebrook</span>
      <span class="secondary">Dental Care</span>
    </h1>
    <div class="service-band"><span class="service">DENTIST</span></div>
    <p class="street">STREET NUMBER: 847</p>
    <p class="phone">
      <svg viewBox="0 0 34 44" aria-hidden="true">
        <path d="M9 2 L14 12 L10 16 C12 24 16 30 22 34 L26 30 L33 37 L28 42 C16 40 4 24 3 8 Z" fill="var(--green-dark)"/>
      </svg>
      <span>6154 3970</span>
    </p>
    <div class="band-bottom"></div>
  </section>

  <section class="sign-small" aria-label="Wall sign">
    <div class="stripe dark" style="top:0"></div>
    <div class="stripe mid" style="top:14px"></div>
    <div class="stripe pale" style="top:24px"></div>
    <div class="brand-mark"></div>
    <h2 class="brand-name">
      <span class="primary">Wattlebrook</span>
      <span class="secondary">Dental Care</span>
    </h2>
    <div class="stripe pale" style="top:158px"></div>
    <div class="stripe mid" style="top:168px"></div>
    <div class="stripe dark" style="top:178px"></div>
  </section>

</body>
</html>
```